VELOTRA Brisbane Tiling Service

My name is Milos Vrenbek i need a business card for a new company. We are wall and floor tilers based in Brisbane, our company is Velotra Brisbane Tiling Service.
We would like a logo from our website used on our cards. Our website is www.velotra-tiles.com.au

I would like my Facebook and Twitter accounts on my card.

Business

Colors
0692cd
3176b5
33a6d7
85cae6

```html
<!DOCTYPE html>
<html lang="en">
<head>
<meta charset="utf-8">
<title>Velotra Brisbane Tiling Service – Business Card</title>
<link href="https://fonts.googleapis.com/css2?family=Lato:wght@400;700&display=swap" rel="stylesheet">
<style>
  :root {
    --blue: #0692cd;
    --blue-deep: #3176b5;
    --blue-mid: #33a6d7;
    --blue-light: #85cae6;
    --ink: #2e2e2e;
    --card-hi: #ffffff;
    --card-lo: #e4e4e4;
    --stage: #2b2b2b;
  }
  * { margin: 0; padding: 0; box-sizing: border-box; }
  html, body { width: 1200px; height: 997px; overflow: hidden; }
  body {
    background: var(--stage);
    font-family: "Lato", Arial, sans-serif;
    color: var(--ink);
    position: relative;
  }
  .card {
    position: absolute;
    left: 220px;
    width: 760px;
    height: 434px;
    background: radial-gradient(ellipse at 40% 35%, var(--card-hi) 0%, #f3f3f3 55%, var(--card-lo) 100%);
    overflow: hidden;
    box-shadow: 0 12px 30px rgba(0,0,0,.45);
  }
  .card--back { top: 40px; }
  .card--front { top: 523px; }
  .card__band { position: absolute; left: 0; bottom: 0; width: 760px; height: 60px; }

  .brand { position: absolute; display: flex; align-items: center; gap: 18px; }
  .brand__mark { width: 96px; height: 96px; background: var(--blue); }
  .brand__text { display: flex; flex-direction: column; }
  .brand__name { font-size: 62px; font-weight: 400; color: var(--blue); line-height: .95; letter-spacing: 1px; }
  .brand__tagline { font-size: 26px; color: var(--ink); line-height: 1.1; }

  .card--back .brand { left: 180px; top: 120px; }
  .website {
    position: absolute; left: 0; right: 0; top: 290px;
    text-align: center; font-size: 19px; font-weight: 700; letter-spacing: 5px; color: #333;
  }

  .card--front .brand { left: 170px; top: 40px; }
  .card--front .brand__mark { width: 84px; height: 84px; }
  .card--front .brand__name { font-size: 54px; }
  .card--front .brand__tagline { font-size: 23px; }

  .person { position: absolute; right: 0; top: 168px; width: 300px; }
  .person__tag { position: relative; height: 46px; }
  .person__tag svg { position: absolute; left: 0; top: 0; }
  .person__name {
    position: absolute; left: 22px; top: 8px;
    font-size: 25px; font-weight: 700; color: #fff;
  }
  .person__phone { margin: 4px 0 0 50px; font-size: 26px; letter-spacing: 2px; color: #333; }

  .contact-tab {
    position: absolute; left: 0; top: 236px; width: 70px; height: 170px;
    background: var(--blue); border-radius: 0 14px 14px 0;
    display: flex; flex-direction: column; justify-content: space-around; align-items: center;
    padding: 10px 0;
  }
  .contact-list { position: absolute; left: 92px; top: 240px; list-style: none; }
  .contact-list li { font-size: 17px; height: 40px; line-height: 40px; color: #333; }
</style>
</head>
<body>

<section class="card card--back" aria-label="Card back">
  <div class="brand">
    <div class="brand__mark"></div>
    <div class="brand__text">
      <span class="brand__name">velotra</span>
      <span class="brand__tagline">brisbane tiling service</span>
    </div>
  </div>
  <p class="website">www.velotra-tiles.com.au</p>
  <svg class="card__band" viewBox="0 0 760 60" aria-hidden="true">
    <rect x="0" y="46" width="760" height="14" fill="#6b6b6b"/>
    <path d="M0 52 L560 52 Q580 52 590 32 Q600 14 630 14 L760 14 L760 52 Z" fill="#5a5a5a"/>
    <path d="M0 56 L570 56 Q590 56 600 36 Q610 20 640 20 L760 20 L760 60 L0 60 Z" fill="var(--blue)"/>
  </svg>
</section>

<section class="card card--front" aria-label="Card front">
  <div class="brand">
    <div class="brand__mark"></div>
    <div class="brand__text">
      <span class="brand__name">velotra</span>
      <span class="brand__tagline">brisbane tiling service</span>
    </div>
  </div>

  <div class="person">
    <div class="person__tag">
      <svg width="300" height="46" viewBox="0 0 300 46" aria-hidden="true">
        <path d="M14 0 H212 L200 46 H14 Q0 46 0 32 V14 Q0 0 14 0 Z" fill="var(--blue)"/>
        <path d="M224 0 H236 L224 46 H212 Z" fill="var(--blue)"/>
        <path d="M248 0 H260 L248 46 H236 Z" fill="var(--blue)"/>
        <path d="M272 0 H300 V46 H260 Z" fill="var(--blue)"/>
      </svg>
      <span class="person__name">Milos Vrenbek</span>
    </div>
    <p class="person__phone">0412555804</p>
  </div>

  <div class="contact-tab" aria-hidden="true">
    <svg width="20" height="26" viewBox="0 0 20 26"><rect x="3" y="1" width="14" height="24" rx="3" fill="none" stroke="#fff" stroke-width="2"/><rect x="6" y="5" width="8" height="13" fill="#fff"/></svg>
    <svg width="26" height="18" viewBox="0 0 26 18"><rect x="1" y="1" width="24" height="16" fill="#fff"/><path d="M1 1 L13 10 L25 1" fill="none" stroke="var(--blue)" stroke-width="2"/></svg>
    <svg width="20" height="20" viewBox="0 0 20 20"><circle cx="10" cy="10" r="8" fill="#fff"/></svg>
    <svg width="20" height="20" viewBox="0 0 20 20"><rect x="2" y="2" width="16" height="16" fill="#fff"/></svg>
  </div>
  <ul class="contact-list">
    <li>07 3555 0194</li>
    <li>info@velotra-tiles.com.au</li>
    <li>Follow/ InfoVelotra</li>
    <li>Page/Velotra Brisbane</li>
  </ul>

  <svg class="card__band" viewBox="0 0 760 60" aria-hidden="true">
    <path d="M0 52 L500 52 Q520 52 530 34 Q540 18 570 18 L760 18 L760 60 L0 60 Z" fill="#5a5a5a"/>
    <path d="M520 60 Q530 40 545 30 Q560 22 590 22 L760 22 L760 60 Z" fill="var(--blue)"/>
  </svg>
</section>

</body>
</html>
```